Home Page Design

Please see design brief attached. Concept here: mockboard[dot]net/file/qr83TpLM5wnePxHbUoKVsY/Velvetcourse---Landing-Page?node-id=0%3A1&t=KPwq7ZnRb2xTcVuM-1

Industry/Entity Type

Wedding

Number of Pages Required

1 page

Font styles to use
Serif
Sans Serif
Decorative
Script

Colors
A7469A
B969AE
D3A5CF
EDDBEB
F8F0F9
6B429C
8869AF
B7A5CE
E3DAEB
F3F0F8

Requirements
Must have
• Please see attached PDF
Nice to have
• Please see attached PDF
Should not have
• Please see attached PDF

```html
<!DOCTYPE html>
<html lang="en">
<head>
<meta charset="utf-8">
<title>Velvetcourse — Wedding Planning Landing Page</title>
<link rel="stylesheet" href="https://fonts.googleapis.com/css2?family=Playfair+Display:wght@400;500&family=Jost:wght@400;500&family=Allura&display=swap">
<style>
:root{
  --plum:#A7469A; --orchid:#B969AE; --lilac:#D3A5CF; --blush:#EDDBEB; --mist:#F8F0F9;
  --violet:#6B429C; --violet-2:#8869AF; --violet-3:#B7A5CE; --violet-4:#E3DAEB; --violet-5:#F3F0F8;
  --footer:#6A3A86; --ink:#2B2230; --grey:#6E6670; --line:#E6E0E7; --white:#FFFFFF;
  --serif:'Playfair Display',Georgia,serif; --sans:'Jost',Arial,sans-serif; --script:'Allura',cursive;
}
*{box-sizing:border-box;margin:0;padding:0}
html,body{width:1200px;height:4967px;overflow:hidden;background:var(--white);color:var(--ink);font-family:var(--sans)}
.page{position:relative;width:1200px;height:4967px}
section,footer{position:absolute;left:0;width:1200px;overflow:hidden}
.abs{position:absolute}
.center{left:0;width:1200px;text-align:center}
.script{font-family:var(--script);color:var(--plum);font-weight:400;line-height:1}
.display{font-family:var(--serif);font-weight:400;text-transform:uppercase;line-height:1.05;letter-spacing:-.5px}
.btn{position:absolute;display:flex;align-items:center;justify-content:center;gap:8px;background:var(--plum);color:var(--white);font-family:var(--sans);font-size:10px;letter-spacing:.6px;text-transform:uppercase}
.photo{position:absolute}

/* hero */
.hero{top:0;height:698px}
.hero-photo{inset:0;background:linear-gradient(100deg,#8f6a52 0%,#c9a68e 30%,#e9d8cc 55%,#f4ece6 75%,#efe2dc 100%)}
.brand{position:absolute;top:58px;left:0;width:1200px;text-align:center;font-family:var(--serif);font-size:22px;color:var(--violet)}
.hero .auth{top:46px;height:31px;width:95px}
.hero .auth.login{left:893px;background:var(--violet)}
.hero .auth.signup{left:995px;background:var(--orchid)}
.hero-copy{position:absolute;left:560px;width:540px;top:270px;text-align:center}
.hero-copy .script{font-size:64px}
.hero-copy .display{font-size:46px;color:var(--ink)}
.hero .explore{left:756px;top:457px;width:156px;height:39px}

/* stats */
.stats{top:698px;height:135px;background:var(--white)}
.stat{position:absolute;top:0;width:195px;height:135px;text-align:center;border-right:1px solid var(--line)}
.stat:first-child{border-left:1px solid var(--line)}
.stat .num{font-family:var(--serif);font-size:36px;color:var(--violet);margin-top:36px}
.stat .label{font-family:var(--serif);font-size:11px;letter-spacing:.6px;color:var(--grey);margin-top:4px;text-transform:uppercase}
.stat.active{background:var(--violet);border:none}
.stat.active .num,.stat.active .label{color:var(--white)}

/* banner */
.banner{top:833px;height:465px}
.banner-photo{inset:0;background:radial-gradient(ellipse at 55% 45%,#b78f79 0%,#7a5546 38%,#3c2a25 75%,#2a1f1d 100%)}
.banner .display{font-size:40px;color:var(--white)}
.banner .sub{font-family:var(--serif);font-size:13px;color:var(--white);text-transform:uppercase;line-height:19px}
.banner .explore{left:521px;top:309px;width:154px;height:37px;border:1px solid var(--lilac)}

/* testimonials */
.reviews{top:1298px;height:602px;background:linear-gradient(180deg,var(--white) 0%,var(--mist) 35%,var(--blush) 100%)}
.section-script{font-size:48px}
.section-title{font-size:32px;color:var(--ink)}
.card{position:absolute;top:212px;width:243px;height:203px;background:var(--white);box-shadow:0 4px 14px rgba(107,66,156,.12);text-align:center;padding:48px 14px 0}
.card .product{position:absolute;left:106px;top:-25px;width:31px;height:44px;border-radius:4px}
.card h3{font-family:var(--serif);font-weight:400;font-size:12px;color:var(--ink)}
.card .stars{color:var(--plum);font-size:13px;letter-spacing:2px;margin-top:2px}
.card p{font-size:11px;line-height:14px;color:var(--grey);margin-top:8px}
.reviewer{position:absolute;top:431px;display:flex;align-items:center;gap:12px}
.reviewer .avatar{width:60px;height:60px;border-radius:50%;border:3px solid var(--white);box-shadow:0 0 0 1px var(--lilac)}
.reviewer strong{display:block;font-weight:400;font-size:12px;color:var(--ink)}
.reviewer span{font-size:10px;color:var(--grey)}
.nav-arrow{position:absolute;top:596px;width:32px;height:32px;border-radius:50%;border:1px solid var(--lilac);background:var(--white);display:flex;align-items:center;justify-content:center}
.dots{position:absolute;top:525px;left:0;width:1200px;display:flex;justify-content:center;gap:8px}
.dots i{width:8px;height:8px;border-radius:50%;border:1px solid var(--lilac)}
.dots i.on{background:var(--plum);border-color:var(--plum)}

/* how it works */
.steps{top:1900px;height:511px;background:var(--white)}
.step-img{position:absolute;top:154px;height:145px}
.step-arrow{position:absolute;top:212px;width:30px;height:30px;border-radius:50%;background:var(--white);box-shadow:0 1px 6px rgba(0,0,0,.2);display:flex;align-items:center;justify-content:center}
.step{position:absolute;top:326px;width:255px}
.step h3{display:flex;align-items:flex-start;gap:8px;font-family:var(--sans);font-weight:500;font-size:12px;color:var(--plum);line-height:14px}
.step h3 b{flex:none;width:22px;height:22px;border-radius:50%;background:var(--plum);color:var(--white);font-weight:400;font-size:11px;display:flex;align-items:center;justify-content:center}
.step h3 em{font-style:normal;padding-top:4px}
.step p{font-size:10px;line-height:14px;color:var(--grey);margin-top:14px}

/* insured band */
.insured{top:2411px;height:319px;background:linear-gradient(90deg,var(--plum),#9c3d92 60%,var(--plum))}
.insured .badge{position:absolute;left:542px;top:-58px;width:116px;height:116px;border-radius:50%;background:var(--white)}
.insured .display{font-size:32px;color:var(--white)}
.insured .sub{font-size:11px;letter-spacing:.3px;color:var(--white);text-transform:uppercase;line-height:17px}

/* marketplace */
.market{top:2730px;height:820px;background:linear-gradient(180deg,var(--white) 0%,var(--mist) 40%,var(--white) 100%)}
.market .view-all{left:968px;top:119px;width:120px;height:39px}
.tile{position:absolute;width:210px;text-align:center}
.tile .ring{width:210px;height:210px;border-radius:50%;border:1px solid var(--lilac);padding:6px}
.tile .ring div{width:100%;height:100%;border-radius:50%;display:flex;align-items:center;justify-content:center;flex-direction:column;gap:6px;color:var(--white);font-family:var(--serif);font-size:15px;text-transform:uppercase;line-height:1.1}
.tile .name{font-family:var(--serif);font-size:13px;text-transform:uppercase;color:var(--ink);margin-top:12px}

/* download */
.download{top:3550px;height:640px;background:var(--white)}
.download .copy{position:absolute;left:600px;width:516px;top:210px;text-align:center}
.download .copy .script{font-size:64px}
.download .copy .display{font-size:35px;color:var(--ink);line-height:1.05}
.download .pdf{left:772px;top:393px;width:171px;height:41px}
.pdf i{width:16px;height:16px;background:var(--white);display:block}

/* instagram */
.insta{top:4190px;height:357px;background:linear-gradient(180deg,var(--white),var(--mist))}
.insta .display{font-size:32px;color:var(--ink)}
.insta-tile{position:absolute;top:166px;width:200px;height:191px}

/* footer */
.site-footer{top:4547px;height:420px;background:var(--footer);color:var(--white)}
.fcol{position:absolute;top:80px}
.fcol h4{font-family:var(--serif);font-weight:400;font-size:15px;margin-bottom:12px}
.fcol ul{list-style:none}
.fcol li{font-size:10px;line-height:19.3px;opacity:.92}
.copyright{position:absolute;bottom:16px;left:0;width:1200px;text-align:center;font-size:10px}
</style>
</head>
<body>
<div class="page">

  <section class="hero">
    <div class="photo hero-photo" role="img" aria-label="Couple embracing on a sunlit rooftop with a floral table behind them"></div>
    <div class="brand">Velvetcourse</div>
    <a class="btn auth login">Log in</a>
    <a class="btn auth signup">Sign up</a>
    <div class="hero-copy">
      <div class="script">Velvetcourse</div>
      <h1 class="display">Be couple who stuck<br>to their budget!</h1>
    </div>
    <a class="btn explore">Explore now</a>
  </section>

  <section class="stats">
    <div class="stat" style="left:210px"><div class="num">700</div><div class="label">Venues</div></div>
    <div class="stat" style="left:405px"><div class="num">1500</div><div class="label">Vendors</div></div>
    <div class="stat active" style="left:600px"><div class="num">500</div><div class="label">Wedding booked</div></div>
    <div class="stat" style="left:795px"><div class="num">$7,680</div><div class="label">Averaged saved</div></div>
  </section>

  <section class="banner">
    <div class="photo banner-photo" role="img" aria-label="Groom placing a ring on the bride's hand beside a bouquet of roses"></div>
    <h2 class="abs center display" style="top:148px">Because life is too short<br>to wait for vendors to reply</h2>
    <p class="abs center sub" style="top:243px">Focus on enjoying your wedding! Don't get tied into<br>endless negotiations and emails.</p>
    <a class="btn explore">Explore now</a>
  </section>

  <section class="reviews">
    <div class="abs center script section-script" style="top:88px">Testimonials</div>
    <h2 class="abs center display section-title" style="top:128px">Our customer loves us</h2>

    <a class="nav-arrow" style="left:144px;top:298px"><svg width="10" height="10" viewBox="0 0 10 10"><path d="M6.5 1.5 3 5l3.5 3.5" fill="none" stroke="#A7469A" stroke-width="1.3"/></svg></a>
    <a class="nav-arrow" style="left:1024px;top:298px"><svg width="10" height="10" viewBox="0 0 10 10"><path d="M3.5 1.5 7 5 3.5 8.5" fill="none" stroke="#A7469A" stroke-width="1.3"/></svg></a>

    <article class="card" style="left:210px">
      <div class="product" style="background:#8a6a3c" role="img" aria-label="Winter jacket product thumbnail"></div>
      <h3>Yara Winter Jacket</h3><div class="stars">★★★★★</div>
      <p>The quality of products are awsome and my kids really love it. Lorem ipsum dolor sit amet, consectetur adipiscing elit. Praesent quis velit vitae ante semper v</p>
    </article>
    <article class="card" style="left:478px">
      <div class="product" style="background:#f0a8b4" role="img" aria-label="Pink t-shirt product thumbnail"></div>
      <h3>Yara Boy T-shirt</h3><div class="stars">★★★★★</div>
      <p>The quality of products are awsome and my kids really love it. Lorem ipsum dolor sit amet, consectetur adipiscing elit. Praesent quis velit vitae ante semper v</p>
    </article>
    <article class="card" style="left:746px">
      <div class="product" style="background:#9db4dc" role="img" aria-label="Patterned fleece product thumbnail"></div>
      <h3>Willow Fleece Cozie</h3><div class="stars">★★★★★</div>
      <p>The quality of products are awsome and my kids really love it. Lorem ipsum dolor sit amet, consectetur adipiscing elit. Praesent quis velit vitae ante semper v</p>
    </article>

    <div class="reviewer" style="left:215px"><div class="avatar" style="background:#d9c3cf" role="img" aria-label="Reviewer portrait"></div><div><strong>Marla Quinn</strong><span>November, 30 2019</span></div></div>
    <div class="reviewer" style="left:485px"><div class="avatar" style="background:#e2c69c" role="img" aria-label="Reviewer portrait"></div><div><strong>Marla Quinn</strong><span>November, 30 2019</span></div></div>
    <div class="reviewer" style="left:751px"><div class="avatar" style="background:#5a4a44" role="img" aria-label="Reviewer portrait"></div><div><strong>Dorian Vale</strong><span>November, 30 2019</span></div></div>

    <div class="dots"><i></i><i class="on"></i><i></i><i></i></div>
  </section>

  <section class="steps">
    <div class="abs center script section-script" style="top:66px">3 step</div>
    <h2 class="abs center display section-title" style="top:100px">How it works</h2>
    <div class="step-img" style="left:208px;width:255px;background:linear-gradient(120deg,#6f5a55,#cbbcb4,#8a7470)" role="img" aria-label="Bride trying on a gown with friends"></div>
    <div class="step-img" style="left:473px;width:254px;background:linear-gradient(120deg,#b9c3cf,#e8e2de,#9aa3ad)" role="img" aria-label="Couple browsing vendors together on a sofa"></div>
    <div class="step-img" style="left:737px;width:253px;background:linear-gradient(120deg,#7b8466,#d8d0c2,#6d6a58)" role="img" aria-label="Groom with groomsmen outdoors"></div>
    <span class="step-arrow" style="left:451px"><svg width="10" height="10" viewBox="0 0 10 10"><path d="M2 2l3 3-3 3M5 2l3 3-3 3" fill="none" stroke="#A7469A" stroke-width="1.1"/></svg></span>
    <span class="step-arrow" style="left:717px"><svg width="10" height="10" viewBox="0 0 10 10"><path d="M2 2l3 3-3 3M5 2l3 3-3 3" fill="none" stroke="#A7469A" stroke-width="1.1"/></svg></span>
    <div class="step" style="left:216px"><h3><b>1</b><em>Browse Top Vendors</em></h3><p>The quality of products are awsome and my kids really love it. Lorem ipsum dolor sit amet, consectetur adipiscing elit. Praesent quis velit vitae ante semper v</p></div>
    <div class="step" style="left:478px"><h3><b>2</b><em>Instantly Book With Pre-<br>Negotiated Prices</em></h3><p>The quality of products are awsome and my kids really love it. Lorem ipsum dolor sit amet, consectetur adipiscing elit. Praesent quis velit vitae ante semper v</p></div>
    <div class="step" style="left:742px"><h3><b>3</b><em>Pay Over Time</em></h3><p>The quality of products are awsome and my kids really love it. Lorem ipsum dolor sit amet, consectetur adipiscing elit. Praesent quis velit vitae ante semper v</p></div>
  </section>

  <section class="insured" style="overflow:visible">
    <h2 class="abs center display" style="top:108px">VelvetWish! - Because life happend<br>all your bookings are fully insured</h2>
    <p class="abs center sub" style="top:196px">Lorem ipsum dolor sit amet, consectetur adipiscing elit. Phasellus eu hendrerit dui, sit amet<br>finibus elit. Aliquam erat volutpat. Nullam eget mauris massa. Quisque mi elit, tincidunt</p>
  </section>
  <div class="abs" style="left:542px;top:2353px;width:116px;height:116px;border-radius:50%;background:var(--white)"></div>

  <section class="market">
    <div class="abs script" style="left:108px;top:88px;font-size:40px">explore</div>
    <h2 class="abs display" style="left:108px;top:112px;font-size:32px">Our marketplace</h2>
    <p class="abs" style="left:110px;top:157px;font-family:var(--serif);font-size:12px;text-transform:uppercase">Lorem ipsum dolor sit amet, consectetur adipiscing elit.</p>
    <a class="btn view-all">View all</a>

    <div class="tile" style="left:119px;top:203px"><div class="ring"><div style="background:radial-gradient(circle,#f4f1ef,#b9aeb0)" role="img" aria-label="Reception table with glassware"></div></div><div class="name">Reception venues</div></div>
    <div class="tile" style="left:370px;top:203px"><div class="ring"><div style="background:radial-gradient(circle,#7a3f86,#3c2344)">
      <svg width="30" height="26" viewBox="0 0 30 26"><rect x="2" y="6" width="26" height="18" rx="3" fill="none" stroke="#fff" stroke-width="1.6"/><rect x="10" y="2" width="10" height="5" rx="1.5" fill="none" stroke="#fff" stroke-width="1.6"/><circle cx="15" cy="15" r="5.5" fill="none" stroke="#fff" stroke-width="1.6"/></svg>
      <span>Wedding<br>photographers</span></div></div></div>
    <div class="tile" style="left:620px;top:203px"><div class="ring"><div style="background:radial-gradient(circle,#d8c7bf,#7e5e52)" role="img" aria-label="Videographer filming a couple under an archway"></div></div><div class="name">Videographers</div></div>
    <div class="tile" style="left:871px;top:203px"><div class="ring"><div style="background:radial-gradient(circle,#c6b2e8,#5a3f8f)" role="img" aria-label="Couple dancing under party lights"></div></div><div class="name">DJs</div></div>

    <div class="tile" style="left:119px;top:475px"><div class="ring"><div style="background:radial-gradient(circle,#9a9a9a,#1e1e1e)" role="img" aria-label="Band performing in black and white"></div></div><div class="name">Wedding bands</div></div>
    <div class="tile" style="left:370px;top:475px"><div class="ring"><div style="background:radial-gradient(circle,#e4d6b0,#4a3c2a)" role="img" aria-label="Planner arranging table decor"></div></div><div class="name">Wedding planners</div></div>
    <div class="tile" style="left:620px;top:475px"><div class="ring"><div style="background:radial-gradient(circle,#f0e6dc,#b39a8a)" role="img" aria-label="Wedding rings on a flower"></div></div><div class="name">Jewelers</div></div>
    <div class="tile" style="left:871px;top:475px"><div class="ring"><div style="background:radial-gradient(circle,#ffffff,#d9d3cf)" role="img" aria-label="Tiered white wedding cake"></div></div><div class="name">Wedding cakes</div></div>
  </section>

  <section class="download">
    <div class="photo" style="left:208px;top:73px;width:504px;height:478px;background:linear-gradient(135deg,#d9e2ea,#b9a396 45%,#e9dcd6)" role="img" aria-label="Bride and groom kissing outdoors with a bouquet"></div>
    <div class="copy">
      <div class="script">Download</div>
      <h2 class="display">Download our free<br>pdf and start down the<br>road to saving money</h2>
    </div>
    <a class="btn pdf"><i></i>Download PDF</a>
  </section>

  <section class="insta">
    <div class="abs center script section-script" style="top:40px">instagram</div>
    <h2 class="abs center display" style="top:78px">Reclaim your<br>sanity-book today!</h2>
    <div class="insta-tile" style="left:0;background:linear-gradient(160deg,#c9b9a8,#6e6054)" role="img" aria-label="Wedding party dancing"></div>
    <div class="insta-tile" style="left:200px;background:linear-gradient(160deg,#ece4e0,#b8a49c)" role="img" aria-label="Bride with a tiara"></div>
    <div class="insta-tile" style="left:400px;background:linear-gradient(160deg,#7f9a5f,#c9a2ad)" role="img" aria-label="Couple under a floral arch"></div>
    <div class="insta-tile" style="left:600px;background:linear-gradient(160deg,#d4cbc4,#8c7a70)" role="img" aria-label="Couple smiling together"></div>
    <div class="insta-tile" style="left:800px;background:linear-gradient(160deg,#e8c9c2,#b58a86)" role="img" aria-label="Close-up of an engagement ring"></div>
    <div class="insta-tile" style="left:1000px;background:linear-gradient(160deg,#bfb6b0,#5c4e48)" role="img" aria-label="Couple celebrating with confetti"></div>
  </section>

  <footer class="site-footer">
    <div class="fcol" style="left:112px"><h4>Local Services</h4>
      <ul><li>Wedding Photographers</li><li>Wedding DJs</li><li>Wedding Hair &amp; Makeup</li><li>Wedding Planners</li><li>Wedding Caterers</li><li>Wedding Florists</li><li>Wedding Videographers</li><li>Wedding Officiants</li><li>Wedding Rentals</li><li>Wedding Photo Booths</li><li>Wedding Bands</li></ul></div>
    <div class="fcol" style="left:276px;top:113px"><ul><li>Wedding Dresses &amp; Attire</li><li>Wedding Cakes</li><li>Wedding Limos / Transportation</li><li>Wedding Musicians / Ceremony Music</li><li>Wedding Decor &amp; Lighting</li><li>Wedding Invitations</li><li>Travel Agents</li><li>Wedding Jewelers</li><li>Wedding Favors &amp; Gifts</li><li>Day Of Wedding Coordinators</li><li>Wedding Dance Lessons</li></ul></div>
    <div class="fcol" style="left:532px"><h4>Digital Services</h4>
      <ul><li>Logo Design</li><li>Portraits &amp; Caricatures</li><li>Video Editing</li><li>Invitation Design</li><li>Image Editing</li><li>Slideshow Videos</li><li>Speechwriting</li><li>Greeting Cards &amp; Videos</li></ul></div>
    <div class="fcol" style="left:721px"><h4>Support</h4>
      <ul><li>Help &amp; Support</li><li>Trust &amp; Safety</li><li>Selling on Velvetcourse</li><li>Buying on Velvetcourse</li></ul></div>
    <div class="fcol" style="left:907px"><h4>More from Velvetcourse</h4>
      <ul><li>Velvetcourse Business</li><li>Velvetcourse Pro</li><li>Careers</li><li>Press &amp; News</li><li>Partnership</li><li>Privacy Policy</li><li>Terms of Service</li></ul></div>
    <p class="copyright">©2023 velvetcourse. All Rights Reserved.</p>
  </footer>

</div>
</body>
</html>
```